Bar Soap Packaging Design for Facial Cleansing Bar

Hi,

I have a business that sells soaps, lotions, and other skincare products and I'd like a design for a box for a bar soap that is primarily for women.

The name of the brand is 'Velmo Shea Blend' and the brand is all about renewal and rejuvenation.

I've attached my logo and photos of packaging for bar soaps that are best sellers in my market.

The box is 3 inches x 2 inches and has a white background.

Info to go on the box:

1. Brand name: Velmo Shea Blend

2. [To go below brand name]: Facial Bar

3. Address: Distributed by Haverlin Trading Ltd, 47 Marlow St., Kingston, Jamaica W.I.

4. Contact: tamsin@velmosheablend.example

5. Net Weight: 3.6 oz /102g

6. Ingredients: glycerine, palmitic acid, sodium chloride, water, cocoa butter, fragrance, AOS, EDTA, vitamin E, color.

7. Directions: Wet face. Lather soap in hands. Gently massage lather onto face and neck. Rinse with water and pat dry with a towel. For day, follow with a sunscreen. At night, follow with a serum and/or moisturizer.

8. Please put a circle somewhere on the front with the words: 'Boosts Hydration 100%' in the circle

9. Batch Code: [please leave space beside 'Batch Code' blank]

10. Best Before: April 2019

11. Please put somewhere on the the front: For Younger Looking Skin

12. Please put somewhere on the front: with Real Cocoa Butter and Vitamin E

Thank you,
Tamsin

Target Market(s)

Women 27 to 60 who are looking for anti-age skincare products that'll make them look younger

Industry/Entity Type

Business

Font styles to use
Sans Serif

Colors

Designer to choose colors to be used in the design.

Requirements
Must have
• The info that I've asked for in the brief
Nice to have
• A design similar to the packaging for the brand of soap 'Odra' that I've attached.
Should not have
• Not sure...

```html
<!DOCTYPE html>
<html lang="en">
<head>
<meta charset="utf-8">
<title>Velmo Shea Blend Facial Bar</title>
<link rel="stylesheet" href="https://fonts.googleapis.com/css2?family=Mulish:wght@400;600;700;800&family=Raleway:wght@500&display=swap">
<style>
  :root {
    --canvas: #ffffff;
    --label-top: #ebbcc6;
    --label-mid: #e3a3b1;
    --label-low: #d27d90;
    --brand-ink: #2e2a8c;
    --variant-ink: #3a1a10;
    --variant-frame: #8f4fb0;
    --deep-rose: #b3284c;
    --rose-ring: rgba(196, 70, 100, 0.55);
    --facial-ink: #8a2436;
    --white: #ffffff;
  }
  * { margin: 0; padding: 0; box-sizing: border-box; }
  html, body { width: 1200px; height: 963px; overflow: hidden; background: var(--canvas); }
  .canvas { position: relative; width: 1200px; height: 963px; }
  .label {
    position: absolute; left: 88px; top: 116px; width: 1002px; height: 666px;
    border-radius: 56px; overflow: hidden;
    background: linear-gradient(170deg, var(--label-top) 0%, var(--label-mid) 55%, var(--label-low) 100%);
    font-family: "Mulish", sans-serif;
  }
  .label-art { position: absolute; inset: 0; }
  .badge {
    position: absolute; left: 216px; top: 184px; width: 256px; height: 256px;
    border-radius: 50%; background: var(--rose-ring);
    display: flex; align-items: center; justify-content: center;
  }
  .badge-core {
    width: 214px; height: 214px; border-radius: 50%; background: var(--deep-rose);
    display: flex; align-items: center; justify-content: center;
  }
  .badge-ring {
    width: 188px; height: 188px; border-radius: 50%; border: 1.5px solid rgba(255,255,255,0.8);
    color: var(--white); text-align: center;
    display: flex; flex-direction: column; align-items: center; justify-content: center;
  }
  .badge-small { font-size: 29px; line-height: 1; }
  .badge-big { font-size: 60px; line-height: 1; letter-spacing: -2px; margin: 4px 0 2px; }
  .brand-name {
    position: absolute; left: 504px; top: 122px; width: 500px; text-align: center;
    font-family: "Raleway", sans-serif; font-weight: 500; font-size: 132px; line-height: 1;
    color: var(--brand-ink); letter-spacing: -2px;
  }
  .variant {
    position: absolute; left: 504px; top: 306px; width: 410px; height: 68px;
    border: 2.5px solid var(--variant-frame); border-radius: 10px;
    display: flex; align-items: center; justify-content: center;
    font-weight: 700; font-size: 44px; color: var(--variant-ink); letter-spacing: 1px;
  }
  .product-type {
    position: absolute; left: 456px; top: 428px; width: 490px; text-align: center;
    font-size: 46px; color: var(--facial-ink); line-height: 1;
  }
  .product-type b { font-weight: 800; }
  .claim {
    position: absolute; left: 456px; top: 476px; width: 490px; height: 54px;
    background: var(--deep-rose); border-radius: 14px; color: var(--white);
    display: flex; align-items: center; justify-content: center; gap: 18px;
    font-size: 35px; font-weight: 400;
  }
  .claim .dot { width: 7px; height: 7px; border-radius: 50%; background: rgba(255,255,255,0.8); }
  .net-weight {
    position: absolute; left: 256px; top: 452px; width: 180px; text-align: center;
    color: var(--white); font-size: 21px; line-height: 1.35;
  }
  .ingredients-line {
    position: absolute; left: 204px; top: 570px; display: flex; align-items: center; gap: 4px;
    color: var(--white); font-size: 42px; white-space: nowrap;
  }
  .vitamin-mark {
    width: 46px; height: 46px; border-radius: 50%; background: var(--deep-rose);
    display: inline-flex; align-items: center; justify-content: center; font-size: 38px;
  }
</style>
</head>
<body>
<div class="canvas">
  <section class="label">
    <svg class="label-art" width="1002" height="666" viewBox="0 0 1002 666">
      <defs>
        <linearGradient id="floral-tone" x1="0" y1="0" x2="1" y2="1">
          <stop offset="0" stop-color="#e48aa0"/>
          <stop offset="0.5" stop-color="#f0c4cf"/>
          <stop offset="1" stop-color="#e9d6d4"/>
        </linearGradient>
        <linearGradient id="leaf-tone" x1="0" y1="0" x2="1" y2="0">
          <stop offset="0" stop-color="#b7c48a" stop-opacity="0.5"/>
          <stop offset="1" stop-color="#b7c48a" stop-opacity="0"/>
        </linearGradient>
      </defs>
      <path role="img" aria-label="Sprig of willow leaves"
            d="M560 60 C680 20 820 40 960 110 C900 140 760 120 620 90 Z" fill="url(#leaf-tone)"/>
      <path role="img" aria-label="Bouquet of pink roses, blue hyacinths and green leaves"
            d="M0 0 H560 C560 120 480 190 330 210 C250 240 220 330 230 430 C200 520 170 600 150 666 H0 Z"
            fill="url(#floral-tone)" opacity="0.9"/>
      <path d="M0 480 C180 470 380 520 560 600 C720 650 880 560 1002 470 V500 C880 600 720 680 540 630 C360 560 180 520 0 520 Z"
            fill="rgba(255,255,255,0.28)"/>
      <path d="M0 500 C200 495 380 540 560 615 C720 665 880 580 1002 490"
            fill="none" stroke="rgba(255,255,255,0.6)" stroke-width="2"/>
    </svg>

    <div class="badge">
      <div class="badge-core">
        <div class="badge-ring">
          <span class="badge-small">Boosts</span>
          <span class="badge-big">100%</span>
          <span class="badge-small">Hydration</span>
        </div>
      </div>
    </div>

    <div class="brand-name">Velmo</div>
    <div class="variant">SHEA BLEND</div>

    <div class="product-type">FACIAL<b>BAR</b></div>
    <div class="claim"><span class="dot"></span>For Younger Looking Skin<span class="dot"></span></div>

    <div class="net-weight">Net Weight<br>3.6 Oz /102G</div>

    <div class="ingredients-line">Real Cocoa Butter And Vitamin <span class="vitamin-mark">E</span></div>
  </section>
</div>
</body>
</html>
```